Marlow Realty Real Estate Brokerage Recruiting Flyer

We are a real estate brokerage looking to hire more real estate agents. We need to list everything we have to offer as a company so real estate agents will join our company. this is our company website: www.Marlowrealty.example .

100% COMMISSION NO MONTHLY FEE
$450 Flat Transaction FEE

What We Offer:
24/7 Office Access
Free E & O Insurance for 1st Year
Free Online CE and PLE
Free 1,000 Business Cards
Free Professional Social Media Marketing
Free Printing, Scanning, and Copies
Free Buyer and Seller Presentation Packages
Free Filquay Cloud Based Document Management Access
Access to our Internal Brokerage Forum
Company Profit Sharing!
Private Offices Available to Rent

*Lead Generation Software with over 3,000 Leads
*10 Leads to Start
* Free Personal CRM and Website
*Restrictions and Rules apply

Company Address:
4817 Amberfield Road
Suite 512
Fairfax, VA 22194
Phone: 703-555-0147
email: info@marlowrealty.example

Target Market(s)

Real Estate Agents

Industry/Entity Type

Real Estate

Colors
0555a3
ffffff

Requirements
Must have
• 100% COMMISSION NO MONTHLY FEE
$450 Flat Transaction FEE

What We Offer:
24/7 Office Access
Free Online CE and PLE
Free 1,000 Business Cards
Company Profit Sharing!

*10 Leads to Start

Company Address:
4817 Amberfield Road
Suite 512
Fairfax, VA 22194
Phone: 703-555-0147

```html
<!DOCTYPE html>
<html lang="en">
<head>
<meta charset="utf-8">
<title>Marlow Realty – Agent Recruiting Flyer</title>
<link href="https://fonts.googleapis.com/css2?family=Questrial&family=Oswald:wght@500;600&family=Open+Sans:wght@700;800&display=swap" rel="stylesheet">
<style>
  :root {
    --brand-blue: #0555a3;
    --deep-blue: #0a3a8c;
    --light-blue: #4fa3f0;
    --ink: #1d1d22;
    --white: #ffffff;
    --panel-grey: #d6d7da;
    --page-bg: #e7e7e9;
  }
  * { box-sizing: border-box; margin: 0; padding: 0; }
  html, body { width: 1200px; height: 1200px; overflow: hidden; background: var(--page-bg); }
  body { position: relative; font-family: "Questrial", sans-serif; color: var(--ink); }

  .flyer {
    position: absolute; left: 200px; top: 35px; width: 800px; height: 1130px;
    background: var(--white); overflow: hidden;
    box-shadow: 0 6px 24px rgba(0,0,0,.18);
  }
  .flyer-art { position: absolute; inset: 0; }

  .brand-box {
    position: absolute; left: 350px; top: 34px; width: 290px; height: 110px;
    background: var(--white); display: flex; align-items: center; justify-content: center; gap: 14px;
    box-shadow: 0 3px 10px rgba(0,0,0,.15);
  }
  .brand-mark { width: 26px; height: 26px; background: var(--deep-blue); }
  .brand-name { font-family: "Questrial", sans-serif; font-size: 32px; color: var(--deep-blue); letter-spacing: 1px; }

  .offer-heading {
    position: absolute; left: 360px; top: 446px; width: 340px; height: 38px;
    background: var(--deep-blue); color: var(--white);
    font-family: "Open Sans", sans-serif; font-weight: 800; font-size: 20px;
    padding: 6px 0 0 28px; letter-spacing: .5px;
  }
  .offer-panel {
    position: absolute; left: 380px; top: 484px; width: 400px; height: 420px;
    border: 3px solid var(--deep-blue); border-top: none; border-radius: 0 0 30px 30px;
    background: linear-gradient(100deg, #ffffff 10%, var(--panel-grey) 100%);
    padding: 14px 20px 0 24px;
  }

  .perk-list { list-style: none; }
  .perk-list li {
    position: relative; padding-left: 28px; font-size: 16.5px; line-height: 1.3; margin-bottom: 7px;
  }
  .perk-list .tick { position: absolute; left: 0; top: 3px; width: 17px; height: 17px; }
  .free-tag {
    display: inline-block; background: var(--brand-blue); color: var(--white);
    font-family: "Open Sans", sans-serif; font-weight: 800; font-size: 12px;
    padding: 0 5px; line-height: 18px; margin-right: 5px; vertical-align: 1px;
    border: 1.5px solid var(--deep-blue); box-shadow: inset 0 0 0 1px rgba(255,255,255,.5);
  }

  .commission-badge {
    position: absolute; left: 62px; top: 520px; width: 320px; height: 320px; border-radius: 50%;
    background: linear-gradient(145deg, #f2f2f2, #9c9ea3);
    padding: 12px; box-shadow: 6px 14px 18px rgba(0,0,0,.2);
  }
  .commission-badge .disc {
    width: 100%; height: 100%; border-radius: 50%;
    background: radial-gradient(circle at 40% 35%, #1a5bc4 0%, var(--deep-blue) 70%, #072a6b 100%);
    display: flex; flex-direction: column; align-items: center; justify-content: center;
    font-family: "Oswald", sans-serif; font-weight: 600; text-transform: uppercase; line-height: 1.05;
  }
  .disc .line-white { color: var(--white); font-size: 34px; }
  .disc .line-blue { color: var(--light-blue); font-size: 34px; }
  .disc .rule { width: 180px; height: 3px; background: var(--white); margin: 8px 0; }

  .extras-list { position: absolute; left: 60px; top: 868px; width: 330px; }

  .footer-rule { position: absolute; left: 0; right: 0; top: 1018px; height: 4px; background: #b9bbbf; }
  .site-footer {
    position: absolute; left: 0; right: 0; bottom: 0; height: 96px; background: var(--deep-blue);
    display: flex; align-items: center; justify-content: space-between; padding: 0 28px;
    color: var(--white); font-size: 14px; line-height: 1.3;
  }
  .contact-item { display: flex; align-items: center; gap: 7px; }
  .contact-item svg { width: 14px; height: 14px; flex: none; }
</style>
</head>
<body>
<main class="flyer">
  <svg class="flyer-art" viewBox="0 0 800 1130" width="800" height="1130" aria-hidden="false">
    <defs>
      <linearGradient id="hero-tone" x1="0" y1="0" x2="1" y2="1">
        <stop offset="0" stop-color="#cfd8e2"/>
        <stop offset=".45" stop-color="#a9b6c4"/>
        <stop offset=".75" stop-color="#8fa39a"/>
        <stop offset="1" stop-color="#6f9a4c"/>
      </linearGradient>
    </defs>
    <path role="img" aria-label="Photo of a smiling agent in a dark suit in front of a row of white suburban homes"
          d="M0,0 H800 V440 Q560,470 360,570 Q180,660 0,740 Z" fill="url(#hero-tone)"/>
    <path d="M0,760 Q180,680 360,590 Q570,480 800,452 V476 Q580,505 380,620 Q190,730 0,820 Z" fill="#0a3a8c"/>
  </svg>

  <div class="brand-box">
    <span class="brand-mark"></span>
    <span class="brand-name">Marlow Realty</span>
  </div>

  <div class="offer-heading">WHAT WE OFFER:</div>
  <section class="offer-panel">
    <ul class="perk-list">
      <li><svg class="tick" viewBox="0 0 20 20"><circle cx="10" cy="10" r="8.5" fill="none" stroke="#0a3a8c" stroke-width="2"/><path d="M6 10.3l2.7 2.7 5-5.2" fill="none" stroke="#0a3a8c" stroke-width="2"/></svg>24/7 Office Access</li>
      <li><svg class="tick" viewBox="0 0 20 20"><circle cx="10" cy="10" r="8.5" fill="none" stroke="#0a3a8c" stroke-width="2"/><path d="M6 10.3l2.7 2.7 5-5.2" fill="none" stroke="#0a3a8c" stroke-width="2"/></svg><span class="free-tag">FREE</span>E &amp; O Insurance for 1st Year</li>
      <li><svg class="tick" viewBox="0 0 20 20"><circle cx="10" cy="10" r="8.5" fill="none" stroke="#0a3a8c" stroke-width="2"/><path d="M6 10.3l2.7 2.7 5-5.2" fill="none" stroke="#0a3a8c" stroke-width="2"/></svg><span class="free-tag">FREE</span>Online CE and PLE</li>
      <li><svg class="tick" viewBox="0 0 20 20"><circle cx="10" cy="10" r="8.5" fill="none" stroke="#0a3a8c" stroke-width="2"/><path d="M6 10.3l2.7 2.7 5-5.2" fill="none" stroke="#0a3a8c" stroke-width="2"/></svg><span class="free-tag">FREE</span>1,000 Business Cards</li>
      <li><svg class="tick" viewBox="0 0 20 20"><circle cx="10" cy="10" r="8.5" fill="none" stroke="#0a3a8c" stroke-width="2"/><path d="M6 10.3l2.7 2.7 5-5.2" fill="none" stroke="#0a3a8c" stroke-width="2"/></svg><span class="free-tag">FREE</span>Professional Social Media Marketing</li>
      <li><svg class="tick" viewBox="0 0 20 20"><circle cx="10" cy="10" r="8.5" fill="none" stroke="#0a3a8c" stroke-width="2"/><path d="M6 10.3l2.7 2.7 5-5.2" fill="none" stroke="#0a3a8c" stroke-width="2"/></svg><span class="free-tag">FREE</span>Printing, Scanning, and Copies</li>
      <li><svg class="tick" viewBox="0 0 20 20"><circle cx="10" cy="10" r="8.5" fill="none" stroke="#0a3a8c" stroke-width="2"/><path d="M6 10.3l2.7 2.7 5-5.2" fill="none" stroke="#0a3a8c" stroke-width="2"/></svg><span class="free-tag">FREE</span>Buyer and Seller Presentation Packages</li>
      <li><svg class="tick" viewBox="0 0 20 20"><circle cx="10" cy="10" r="8.5" fill="none" stroke="#0a3a8c" stroke-width="2"/><path d="M6 10.3l2.7 2.7 5-5.2" fill="none" stroke="#0a3a8c" stroke-width="2"/></svg><span class="free-tag">FREE</span>Filquay Cloud Based Document Management Access</li>
      <li><svg class="tick" viewBox="0 0 20 20"><circle cx="10" cy="10" r="8.5" fill="none" stroke="#0a3a8c" stroke-width="2"/><path d="M6 10.3l2.7 2.7 5-5.2" fill="none" stroke="#0a3a8c" stroke-width="2"/></svg>Access to our Internal Brokerage Forum</li>
      <li><svg class="tick" viewBox="0 0 20 20"><circle cx="10" cy="10" r="8.5" fill="none" stroke="#0a3a8c" stroke-width="2"/><path d="M6 10.3l2.7 2.7 5-5.2" fill="none" stroke="#0a3a8c" stroke-width="2"/></svg>Company Profit Sharing!</li>
      <li><svg class="tick" viewBox="0 0 20 20"><circle cx="10" cy="10" r="8.5" fill="none" stroke="#0a3a8c" stroke-width="2"/><path d="M6 10.3l2.7 2.7 5-5.2" fill="none" stroke="#0a3a8c" stroke-width="2"/></svg>Private Offices Available to Rent</li>
    </ul>
  </section>

  <div class="commission-badge">
    <div class="disc">
      <span class="line-white">100% Commission</span>
      <span class="line-blue">No Monthly Fee</span>
      <span class="rule"></span>
      <span class="line-white">$450 Flat</span>
      <span class="line-blue">Transaction Fee</span>
    </div>
  </div>

  <ul class="perk-list extras-list">
    <li><svg class="tick" viewBox="0 0 20 20"><circle cx="10" cy="10" r="8.5" fill="none" stroke="#0a3a8c" stroke-width="2"/><path d="M6 10.3l2.7 2.7 5-5.2" fill="none" stroke="#0a3a8c" stroke-width="2"/></svg>Lead Generation Software with over 3,000 Leads</li>
    <li><svg class="tick" viewBox="0 0 20 20"><circle cx="10" cy="10" r="8.5" fill="none" stroke="#0a3a8c" stroke-width="2"/><path d="M6 10.3l2.7 2.7 5-5.2" fill="none" stroke="#0a3a8c" stroke-width="2"/></svg>10 Leads to Start</li>
    <li><svg class="tick" viewBox="0 0 20 20"><circle cx="10" cy="10" r="8.5" fill="none" stroke="#0a3a8c" stroke-width="2"/><path d="M6 10.3l2.7 2.7 5-5.2" fill="none" stroke="#0a3a8c" stroke-width="2"/></svg><span class="free-tag">FREE</span>Personal CRM and Website</li>
    <li><svg class="tick" viewBox="0 0 20 20"><circle cx="10" cy="10" r="8.5" fill="none" stroke="#0a3a8c" stroke-width="2"/><path d="M6 10.3l2.7 2.7 5-5.2" fill="none" stroke="#0a3a8c" stroke-width="2"/></svg>Restrictions and Rules apply</li>
  </ul>

  <div class="footer-rule"></div>
  <footer class="site-footer">
    <div class="contact-item">
      <svg viewBox="0 0 16 16"><path d="M8 1a5 5 0 0 0-5 5c0 3.6 5 9 5 9s5-5.4 5-9a5 5 0 0 0-5-5zm0 7a2 2 0 1 1 0-4 2 2 0 0 1 0 4z" fill="#fff"/></svg>
      <span>4817 Amberfield Road<br>Suite 512 Fairfax, VA 22194</span>
    </div>
    <div class="contact-item">
      <svg viewBox="0 0 16 16"><path d="M4 1.5l2.3 3-1.4 1.6c.8 1.9 2.2 3.3 4 4l1.6-1.4 3 2.3-1.3 2.4C7.3 13.4 2.6 8.7 1.6 3z" fill="#fff"/></svg>
      <span>703-555-0147</span>
    </div>
    <div class="contact-item">
      <svg viewBox="0 0 16 16"><rect x="1" y="3" width="14" height="10" fill="none" stroke="#fff" stroke-width="1.5"/><path d="M1 3l7 6 7-6" fill="none" stroke="#fff" stroke-width="1.5"/></svg>
      <span>info@marlowrealty.example</span>
    </div>
    <div class="contact-item">
      <svg viewBox="0 0 16 16"><circle cx="8" cy="8" r="6.5" fill="none" stroke="#fff" stroke-width="1.4"/><path d="M1.5 8h13M8 1.5c-3 3.5-3 9.5 0 13M8 1.5c3 3.5 3 9.5 0 13" fill="none" stroke="#fff" stroke-width="1.2"/></svg>
      <span>www.Marlowrealty.example</span>
    </div>
  </footer>
</main>
</body>
</html>
```